Riverbend Haven Home Care-Nursing Assessment Form

I am creating a Nursing Assessment Form (which is used to be an intake form for all new patients) for my new home care company, Riverbend Haven Home Care.

It is 15 pages and pretty comprehensive as this is a very regulated field. I have all the necessary content and information attached in the word document below. Now, I am seeking a designer to make it look professional, cohesive and easy to read/ follow.
In order for your Word Document Design to be selected, you must:

1. As mentioned previously, make it easy to read/follow. There should be enough spacing, room to write out all necessary notes, fill out check marks...etc...
2. It should look professional.
3. It should be attractive and eye pleasing. Attached you will find our logo-kindly incorporate it's style into the project as well. The logo should be placed on top of each page.
4. Lastly, we need a Word Document version AND PDF Fillable Option. The fillable PDF should Auto Fill for the Name and Start of Care (SOC) Date.

I have attached a sample form below as well. This is how I envision the finished project to look. Of course, I am open to other suggestions as look as it meets the aforementioned requirements.

Thank you! May the best man or woman win!
Our team looks forward to working with our designer on this project!

Industry/Entity Type

Home Health Care

Font styles to use
Sans Serif

Colors
0255a3
9bcb3c

Requirements
Must have
• Refer to Project Description above.
Nice to have
We must be given a Word Document Option and PDF Fillable Option.

```html
<!DOCTYPE html>
<html lang="en">
<head>
<meta charset="utf-8">
<title>Riverbend Haven Home Care – Fillable Forms</title>
<link href="https://fonts.googleapis.com/css2?family=Montserrat:wght@300;400;500;600;700&display=swap" rel="stylesheet">
<style>
  :root{
    --bg:#c8ced2;
    --green:#8dc63f;
    --blue:#0255a3;
    --panel:#eeeeee;
    --field-border:#cfcfcf;
    --label:#4a4a4a;
    --muted:#8a8a8a;
    --white:#ffffff;
  }
  html,body{margin:0;padding:0;width:800px;height:1200px;overflow:hidden;background:var(--bg);font-family:'Montserrat',sans-serif}
  .stage{position:relative;width:1000px;height:1500px;transform:scale(.8);transform-origin:0 0}
  .board-title{position:absolute;top:44px;left:0;width:1000px;text-align:center;margin:0;
    font:400 82px/1 'Montserrat',sans-serif;letter-spacing:14px;color:transparent;
    -webkit-text-stroke:1.6px var(--white)}
  .spread{position:absolute;left:63px;top:189px;width:866px;height:609px;box-shadow:0 14px 28px rgba(0,0,0,.22)}
  .spread::after{content:"";position:absolute;left:431px;top:0;width:4px;height:100%;background:linear-gradient(90deg,rgba(0,0,0,.06),rgba(0,0,0,0))}
  .page{position:absolute;width:433px;height:609px;background:var(--white);padding:0 20px;box-sizing:border-box;color:var(--label)}
  .spread .page.left{left:0;top:0}
  .spread .page.right{left:433px;top:0}
  .page.solo-left{left:61px;top:864px;width:428px;height:605px}
  .page.solo-right{left:511px;top:864px;width:428px;height:605px}

  .head{position:relative;height:66px}
  .head h1{position:absolute;top:21px;left:0;margin:0;font:700 14.5px/18px 'Montserrat',sans-serif;color:var(--green);letter-spacing:.2px}
  .head::after{content:"";position:absolute;left:0;right:0;top:61px;height:1px;background:var(--green)}
  .brand{position:absolute;right:0;top:34px;display:flex;align-items:center;gap:4px;font:700 7px 'Montserrat',sans-serif;color:var(--blue)}
  .brand .dot{width:18px;height:18px;border-radius:50%;background:var(--blue)}

  .box{background:var(--panel);padding:4px 4px 2px;margin-top:8px}
  .box + .box{margin-top:12px}
  .box h2{margin:2px 0 8px;font:600 11px 'Montserrat',sans-serif;color:var(--blue)}
  .box h2.sub{margin-top:10px}
  .row{display:flex;gap:20px;margin-bottom:7px}
  .row.tight{gap:6px}
  .f{flex:1;min-width:0}
  .f span{display:block;font:500 6.5px/8px 'Montserrat',sans-serif;color:var(--label);margin-bottom:2px;white-space:nowrap}
  .f i{display:block;height:10px;background:var(--white);border:1px solid var(--field-border);border-radius:2px}
  .f i.tall{height:34px}
  .f .pair{display:flex;gap:3px}
  .f .pair i{flex:1}

  .opts{display:flex;align-items:center;gap:11px;font:400 6.5px 'Montserrat',sans-serif;color:var(--muted);margin:2px 0 9px}
  .opts b{font-weight:500;color:var(--label)}
  .opts .push{margin-left:auto}
  .r{display:inline-flex;align-items:center;gap:4px;white-space:nowrap}
  .r::before{content:"";width:7px;height:7px;border-radius:50%;border:1px solid var(--field-border);background:var(--white)}

  .hazards{display:grid;grid-template-columns:1fr 1fr;row-gap:4px;font:400 6.3px 'Montserrat',sans-serif;color:var(--muted);margin-bottom:10px}

  .ability{display:flex;gap:14px;padding-bottom:4px}
  .ability .list{width:210px}
  .ab-row{display:flex;align-items:center;height:18px;font:500 6.3px/7px 'Montserrat',sans-serif;color:var(--label)}
  .ab-row .lbl{flex:1}
  .ab-row .r{color:var(--muted);font-weight:400;margin-left:10px}
  .ability .comments{flex:1}
  .ability .comments i{height:94px}
</style>
</head>
<body>
<div class="stage">
  <h1 class="board-title">FILLABLE FORMS</h1>

  <div class="spread">
    <!-- Page: patient details -->
    <section class="page left">
      <header class="head">
        <h1>Riverbend Haven Home Care<br>Initial Assessment Form</h1>
        <div class="brand"><span class="dot"></span>RIVERBEND HAVEN</div>
      </header>
      <div class="box">
        <div class="row"><div class="f" style="flex:3"><span>Name</span><i></i></div><div class="f"><span>SOC Date</span><i></i></div></div>
      </div>
      <div class="box">
        <h2>Patient Details</h2>
        <div class="row"><div class="f" style="flex:3"><span>Name of the Patient</span><i></i></div><div class="f"><span>Gender</span><i></i></div></div>
        <div class="row"><div class="f" style="flex:1.5"><span>Primary Diagnosis</span><i></i></div><div class="f" style="flex:1.5"><span>Secondary Diagnosis</span><i></i></div><div class="f"><span>MR#</span><i></i></div></div>
        <div class="row"><div class="f" style="flex:1.5"><span>Other Pertinent Diagnosis</span><i></i></div><div class="f" style="flex:1.5"><span>PCP name</span><i></i></div><div class="f"><span>Date</span><i></i></div></div>
        <div class="row"><div class="f"><span>Other Physician Name</span><i></i></div></div>
        <div class="opts"><b>Prognosis</b><span class="r">Poor</span><span class="r">Fair</span><span class="r">Good</span><span class="r">Excellent</span></div>
        <div class="row tight"><div class="f"><span>Height</span><i></i></div><div class="f"><span>Weight</span><i></i></div><div class="f"><span>Temp</span><i></i></div><div class="f"><span>Pulse</span><i></i></div><div class="f"><span>Resp</span><i></i></div><div class="f"><span>B/P</span><i></i></div></div>
        <div class="row"><div class="f"><span>Allergies</span><i></i></div></div>
        <div class="row"><div class="f"><span>Past Medical and Surgical History</span><i class="tall"></i></div></div>
      </div>
      <div class="box">
        <h2>Support System</h2>
        <div class="opts"><span class="r">Married</span><span class="r">Not Married</span><span class="r">Single</span><span class="r">Divorced</span><span class="r">Widowed</span><b class="push">Lives Alone</b><span class="r">Yes</span><span class="r">No</span></div>
        <div class="row"><div class="f"><span>Family Composition</span><i></i></div></div>
        <div class="row"><div class="f" style="flex:1.6"><span>Legal Next of Kin</span><i></i></div><div class="f" style="flex:1.6"><span>Telephone</span><div class="pair"><i></i><i></i></div></div></div>
        <div class="row"><div class="f" style="flex:2"><span>Address</span><i></i></div><div class="f"><span>E-mail</span><i></i></div></div>
        <div class="opts"><b>Is significant other able, available, capable and willing to care for patient?</b><span class="r">Yes</span><span class="r">No</span></div>
        <div class="row"><div class="f"><span>If No, explain</span><i></i></div></div>
        <div class="row"><div class="f"><span>Educational Needs of Patient/Family</span><i></i></div></div>
      </div>
    </section>

    <!-- Page: environment -->
    <section class="page right">
      <header class="head">
        <h1>Riverbend Haven Home Care<br>Initial Assessment Form</h1>
        <div class="brand"><span class="dot"></span>RIVERBEND HAVEN</div>
      </header>
      <div class="box">
        <div class="row"><div class="f" style="flex:3"><span>Name</span><i></i></div><div class="f"><span>SOC Date</span><i></i></div></div>
      </div>
      <div class="box">
        <h2>Environment</h2>
        <div class="opts"><span class="r">Private Home</span><span class="r">Apartment</span><span class="r">Elevator</span><span class="r">Walkup</span></div>
        <h2 class="sub">Safety Hazards in the Home</h2>
        <div class="hazards">
          <span class="r">Sound structure</span><span class="r">Safe Placement of Cords, Rugs and Furniture</span>
          <span class="r">Adequate Heating and Ventilation</span><span class="r">Adequate Cooking facility</span>
          <span class="r">Adequate Plumbing/Sanitation/ Running Water</span><span class="r">Adequate Sleeping Arrangement</span>
          <span class="r">Safe Gas/Electric Appliances</span><span class="r">Grounded Plug for Equipment</span>
          <span class="r">Enough Electrical Outlets for Equipment</span><span class="r">Working Telephone in the Home</span>
          <span class="r">Safe storage for Supplies/Equipment/Meds</span><span class="r">Exits Free of Obstruction</span>
          <span class="r">Working smoke detectors</span><span class="r">Fire extinguisher in home</span>
          <span class="r">Infestations of pests</span><span class="r">Neighborhood safe</span>
        </div>
        <div class="row"><div class="f"><span>Comments</span><i class="tall"></i></div></div>
      </div>
      <div class="box">
        <h2>Caregiver’s Contact Information</h2>
        <div class="row"><div class="f" style="flex:1.6"><span>Name</span><i></i></div><div class="f"><span>Telephone</span><div class="pair"><i></i><i></i></div></div></div>
        <div class="row"><div class="f" style="flex:1.6"><span>Address</span><i></i></div><div class="f"><span>E-mail</span><i></i></div></div>
        <div class="row"><div class="f"><span>Days / Time Available</span><i></i></div></div>
      </div>
      <div class="box">
        <h2>Caregivers Ability to Assist Patient / Able to Provide</h2>
        <div class="ability">
          <div class="list">
            <div class="ab-row"><span class="lbl">Personal Care</span><span class="r">Yes</span><span class="r">No</span></div>
            <div class="ab-row"><span class="lbl">Mobility</span><span class="r">Yes</span><span class="r">No</span></div>
            <div class="ab-row"><span class="lbl">Prepare/Serve Meals</span><span class="r">Yes</span><span class="r">No</span></div>
            <div class="ab-row"><span class="lbl">Maintain Safe/Clean Environment</span><span class="r">Yes</span><span class="r">No</span></div>
            <div class="ab-row"><span class="lbl">Perform/ Assist with Procedures</span><span class="r">Yes</span><span class="r">No</span></div>
            <div class="ab-row"><span class="lbl">Caregiver has capacity to learn therapeutic regimen</span><span class="r">Yes</span><span class="r">No</span></div>
          </div>
          <div class="f comments"><span>Comments</span><i></i></div>
        </div>
      </div>
    </section>
  </div>

  <!-- Single page: patient details -->
  <section class="page solo-left">
    <header class="head">
      <h1>Riverbend Haven Home Care<br>Initial Assessment Form</h1>
      <div class="brand"><span class="dot"></span>RIVERBEND HAVEN</div>
    </header>
    <div class="box">
      <div class="row"><div class="f" style="flex:3"><span>Name</span><i></i></div><div class="f"><span>SOC Date</span><i></i></div></div>
    </div>
    <div class="box">
      <h2>Patient Details</h2>
      <div class="row"><div class="f" style="flex:3"><span>Name of the Patient</span><i></i></div><div class="f"><span>Gender</span><i></i></div></div>
      <div class="row"><div class="f" style="flex:1.5"><span>Primary Diagnosis</span><i></i></div><div class="f" style="flex:1.5"><span>Secondary Diagnosis</span><i></i></div><div class="f"><span>MR#</span><i></i></div></div>
      <div class="row"><div class="f" style="flex:1.5"><span>Other Pertinent Diagnosis</span><i></i></div><div class="f" style="flex:1.5"><span>PCP name</span><i></i></div><div class="f"><span>Date</span><i></i></div></div>
      <div class="row"><div class="f"><span>Other Physician Name</span><i></i></div></div>
      <div class="opts"><b>Prognosis</b><span class="r">Poor</span><span class="r">Fair</span><span class="r">Good</span><span class="r">Excellent</span></div>
      <div class="row tight"><div class="f"><span>Height</span><i></i></div><div class="f"><span>Weight</span><i></i></div><div class="f"><span>Temp</span><i></i></div><div class="f"><span>Pulse</span><i></i></div><div class="f"><span>Resp</span><i></i></div><div class="f"><span>B/P</span><i></i></div></div>
      <div class="row"><div class="f"><span>Allergies</span><i></i></div></div>
      <div class="row"><div class="f"><span>Past Medical and Surgical History</span><i class="tall"></i></div></div>
    </div>
    <div class="box">
      <h2>Support System</h2>
      <div class="opts"><span class="r">Married</span><span class="r">Not Married</span><span class="r">Single</span><span class="r">Divorced</span><span class="r">Widowed</span><b class="push">Lives Alone</b><span class="r">Yes</span><span class="r">No</span></div>
      <div class="row"><div class="f"><span>Family Composition</span><i></i></div></div>
      <div class="row"><div class="f" style="flex:1.6"><span>Legal Next of Kin</span><i></i></div><div class="f" style="flex:1.6"><span>Telephone</span><div class="pair"><i></i><i></i></div></div></div>
      <div class="row"><div class="f" style="flex:2"><span>Address</span><i></i></div><div class="f"><span>E-mail</span><i></i></div></div>
      <div class="opts"><b>Is significant other able, available, capable and willing to care for patient?</b><span class="r">Yes</span><span class="r">No</span></div>
      <div class="row"><div class="f"><span>If No, explain</span><i></i></div></div>
      <div class="row"><div class="f"><span>Educational Needs of Patient/Family</span><i></i></div></div>
    </div>
  </section>

  <!-- Single page: environment -->
  <section class="page solo-right">
    <header class="head">
      <h1>Riverbend Haven Home Care<br>Initial Assessment Form</h1>
      <div class="brand"><span class="dot"></span>RIVERBEND HAVEN</div>
    </header>
    <div class="box">
      <div class="row"><div class="f" style="flex:3"><span>Name</span><i></i></div><div class="f"><span>SOC Date</span><i></i></div></div>
    </div>
    <div class="box">
      <h2>Environment</h2>
      <div class="opts"><span class="r">Private Home</span><span class="r">Apartment</span><span class="r">Elevator</span><span class="r">Walkup</span></div>
      <h2 class="sub">Safety Hazards in the Home</h2>
      <div class="hazards">
        <span class="r">Sound structure</span><span class="r">Safe Placement of Cords, Rugs and Furniture</span>
        <span class="r">Adequate Heating and Ventilation</span><span class="r">Adequate Cooking facility</span>
        <span class="r">Adequate Plumbing/Sanitation/ Running Water</span><span class="r">Adequate Sleeping Arrangement</span>
        <span class="r">Safe Gas/Electric Appliances</span><span class="r">Grounded Plug for Equipment</span>
        <span class="r">Enough Electrical Outlets for Equipment</span><span class="r">Working Telephone in the Home</span>
        <span class="r">Safe storage for Supplies/Equipment/Meds</span><span class="r">Exits Free of Obstruction</span>
        <span class="r">Working smoke detectors</span><span class="r">Fire extinguisher in home</span>
        <span class="r">Infestations of pests</span><span class="r">Neighborhood safe</span>
      </div>
      <div class="row"><div class="f"><span>Comments</span><i class="tall"></i></div></div>
    </div>
    <div class="box">
      <h2>Caregiver’s Contact Information</h2>
      <div class="row"><div class="f" style="flex:1.6"><span>Name</span><i></i></div><div class="f"><span>Telephone</span><div class="pair"><i></i><i></i></div></div></div>
      <div class="row"><div class="f" style="flex:1.6"><span>Address</span><i></i></div><div class="f"><span>E-mail</span><i></i></div></div>
      <div class="row"><div class="f"><span>Days / Time Available</span><i></i></div></div>
    </div>
    <div class="box">
      <h2>Caregivers Ability to Assist Patient / Able to Provide</h2>
      <div class="ability">
        <div class="list">
          <div class="ab-row"><span class="lbl">Personal Care</span><span class="r">Yes</span><span class="r">No</span></div>
          <div class="ab-row"><span class="lbl">Mobility</span><span class="r">Yes</span><span class="r">No</span></div>
          <div class="ab-row"><span class="lbl">Prepare/Serve Meals</span><span class="r">Yes</span><span class="r">No</span></div>
          <div class="ab-row"><span class="lbl">Maintain Safe/Clean Environment</span><span class="r">Yes</span><span class="r">No</span></div>
          <div class="ab-row"><span class="lbl">Perform/ Assist with Procedures</span><span class="r">Yes</span><span class="r">No</span></div>
          <div class="ab-row"><span class="lbl">Caregiver has capacity to learn therapeutic regimen</span><span class="r">Yes</span><span class="r">No</span></div>
        </div>
        <div class="f comments"><span>Comments</span><i></i></div>
      </div>
    </div>
  </section>
</div>
</body>
</html>
```